Pill Empires and the Decay of Healing: What Every Patient Should See

brindlemart lumen pub and print on demand. Here are similar books with terrible covers: https://www.brindlemart.example/Fatal-Remedies-Hidden-Racket-Clinics/dp/5512093377
https://www.brindlemart.example/Anxious-Patient-Refill-Overdiagnosed-Nation/dp/5512093385
https://www.brindlemart.example/Crooked-Tablets-Firms-Deceive-Clinicians/dp/5512093393
https://www.brindlemart.example/s/?ie=UTF8&keywords=dosefall&tag=srchlnk-20&index=aps&hvadid=504219837761&hvpos=1t1&hvnetw=g&hvrand=60427719385042277163&hvpone=&hvptwo=&hvqmt=e&hvdev=c&hvdvcmdl=&hvlocint=&hvlocphy=4470288&hvtargid=kwd-73018845521&ref=pd_sl_4k208tqrab_e
https://www.brindlemart.example/Overloaded-Wards-Pledge-Western-Healing/dp/5512093407
https://www.brindlemart.example/Snared-Vocation-Chemical-Inquiries-Liberal-Arts/dp/5512093415
https://www.brindlemart.example/dp/Q77R3K9M2T/ref=dp-lumen-redirect?_encoding=UTF8&btkr=1
https://www.brindlemart.example/Sultans-Bare-Pills-Cracking-Mood-Tablet/dp/5512093423
https://www.brindlemart.example/Lethal-Asylum-Planned-Silence-Varnholt-ebook/dp/Q82V5L1N4W

Help! you can do better than this!

Sick

Target Market(s)

medical readers science readers

Colors

Designer to choose colors to be used in the design.

Requirements
Must have
• great eye catching cover here is excerpt
• As my insight grew, I discovered patient after patient who was broken on the torture-wheel of our therapies, their lives ruined by toxic drugs or surgery. I saw men with back pain which likely would have been self-limited turned into struggling opioid addicts by our promiscuous prescribing culture. Some had surgery supported by no more science than a bar stabbing. I saw people taking ten or more prescriptions. I saw depression and intellectual decline with statin and beta blocker combinations. I saw irreversible brain damage from psychiatric drugs. I saw a lot more.
• As I learned, I felt obliged to share my discoveries, so I began to write. I will take you through my journey step by step. I use quotes, links, and explanatory footnotes liberally to make authentication easy. As you start to grasp the tragedy, you will realize why I cannot sugar-coat or use euphemisms.
Nice to have
• reasonable dignity (no gravestones) but this is a serious subject
• it's freaking a terrible situation
• hope you can do better than the other examples

```html
<!DOCTYPE html>
<html lang="en">
<head>
<meta charset="utf-8">
<title>Pill Empires and the Decay of Healing</title>
<link href="https://fonts.googleapis.com/css2?family=Oswald:wght@600&family=Pathway+Gothic+One&family=Lato:wght@400&display=swap" rel="stylesheet">
<style>
  :root {
    --cover-bg: #000000;
    --ink: #ffffff;
    --pill-white: #f1f2ee;
    --pill-cream: #efe3b4;
    --pill-amber: #dca035;
    --pill-teal: #4fb3b8;
    --pill-pink: #f2b8c0;
  }
  html, body {
    margin: 0;
    padding: 0;
    width: 800px;
    height: 1200px;
    overflow: hidden;
    background: var(--cover-bg);
  }
  .cover {
    position: relative;
    width: 800px;
    height: 1200px;
    background: var(--cover-bg);
    color: var(--ink);
    overflow: hidden;
  }
  .title {
    position: absolute;
    top: 86px;
    left: 0;
    width: 100%;
    margin: 0;
    text-align: center;
    font-family: "Oswald", "Arial Narrow", sans-serif;
    font-weight: 600;
    font-size: 70px;
    line-height: 80px;
    letter-spacing: -0.5px;
    text-transform: uppercase;
  }
  .title span { display: block; }
  .subtitle {
    position: absolute;
    top: 252px;
    left: 0;
    width: 100%;
    margin: 0;
    text-align: center;
    font-family: "Pathway Gothic One", "Arial Narrow", sans-serif;
    font-weight: 400;
    font-size: 44px;
    letter-spacing: 1px;
  }
  .artwork {
    position: absolute;
    top: 360px;
    left: 20px;
    width: 760px;
    height: 730px;
  }
  .author {
    position: absolute;
    top: 1094px;
    left: 0;
    width: 100%;
    margin: 0;
    text-align: center;
    font-family: "Lato", "Helvetica", sans-serif;
    font-weight: 400;
    font-size: 44px;
    letter-spacing: -1px;
    text-transform: uppercase;
  }
</style>
</head>
<body>
  <main class="cover">
    <h1 class="title">
      <span>Pill Empires and the</span>
      <span>Decay of Healing</span>
    </h1>
    <p class="subtitle">What Every Patient Should See</p>

    <svg class="artwork" viewBox="0 0 760 730" role="img"
         aria-label="Illustration of a skull built from white tablets and colourful teal, amber, cream and pink capsules, with loose pills scattered along the bottom">
      <defs>
        <radialGradient id="pill-tones" cx="50%" cy="46%" r="50%">
          <stop offset="0%" stop-color="#f1f2ee"/>
          <stop offset="22%" stop-color="#efe3b4"/>
          <stop offset="42%" stop-color="#dca035"/>
          <stop offset="60%" stop-color="#4fb3b8"/>
          <stop offset="78%" stop-color="#1d3a3c"/>
          <stop offset="100%" stop-color="#000000"/>
        </radialGradient>
      </defs>
      <rect x="0" y="0" width="760" height="730" fill="url(#pill-tones)"/>
    </svg>

    <p class="author">Martin Kessel</p>
  </main>
</body>
</html>
```